Prescription Savings Card

Looking to revamp our cards that are distributed to pharmacies. Processing information must stand out and be in black with lines through zeros for easy identification.
I have included some previous card designs for consideration. we are looking to go with something cleaner with mainly processing information on the back similar to all white version attached.
Target Market(s)
Pharmacists and Pharmacy Technicians
Industry/Entity Type
prescription medications
Contact Information for Business Card
processing information
Requirements
Must have
- easy to read processing information

```html
<!DOCTYPE html>
<html lang="en">
<head>
<meta charset="utf-8">
<title>MedaSave Prescription Savings Card</title>
<link rel="stylesheet" href="https://fonts.googleapis.com/css2?family=Montserrat:wght@600;700;800;900&family=Roboto:wght@400;700&family=Roboto+Mono:wght@700&display=swap">
<style>
  :root {
    --ink: #000000;
    --paper: #e6e7e9;
    --info-panel: #f4f4f5;
    --red: #ec1c24;
    --orange: #fbb040;
    --navy: #2e3192;
    --violet: #4650d8;
    --cyan: #27aae1;
    --white: #ffffff;
    --label-grey: #a7a9ac;
    --stage-light: #fbfbfb;
    --stage-dark: #c9cacc;
  }
  html, body {
    margin: 0;
    padding: 0;
    overflow: hidden;
  }
  .stage {
    position: relative;
    width: 1200px;
    height: 1000px;
    overflow: hidden;
    background: linear-gradient(135deg, var(--stage-light) 0%, var(--stage-dark) 100%);
    font-family: "Montserrat", sans-serif;
  }
  .card {
    position: absolute;
    width: 630px;
    height: 385px;
    filter: drop-shadow(6px 8px 6px rgba(0,0,0,0.35));
  }
  .card--front { left: 119px; top: 70px; }
  .card--back { left: 474px; top: 546px; }
  .side-label {
    position: absolute;
    margin: 0;
    font-family: "Montserrat", sans-serif;
    font-weight: 700;
    font-size: 30px;
    letter-spacing: 1px;
    color: var(--label-grey);
  }
  .side-label--front { left: 836px; top: 258px; }
  .side-label--back { left: 277px; top: 730px; }
  .tagline { font-family: "Montserrat", sans-serif; font-weight: 800; fill: var(--ink); }
  .brand-name { font-family: "Montserrat", sans-serif; font-weight: 900; fill: var(--navy); }
  .notice { font-family: "Montserrat", sans-serif; font-weight: 700; fill: var(--white); }
  .web-address { font-family: "Montserrat", sans-serif; font-weight: 800; fill: #3b4aa8; }
  .feature { font-family: "Montserrat", sans-serif; font-weight: 800; font-size: 14px; fill: var(--white); }
  .proc-label { font-family: "Montserrat", sans-serif; font-weight: 800; font-size: 20px; fill: var(--ink); letter-spacing: 0.5px; }
  .proc-value { font-family: "Roboto Mono", monospace; font-weight: 700; font-size: 20px; fill: var(--ink); }
  .pharmacy-title { font-family: "Montserrat", sans-serif; font-weight: 700; font-size: 16px; fill: var(--white); }
  .pharmacy-note { font-family: "Roboto", sans-serif; font-weight: 400; font-size: 11.5px; fill: var(--white); }
  .pharmacy-note .strong { font-weight: 700; }
</style>
</head>
<body>
<main class="stage">

  <svg class="card card--front" viewBox="0 0 630 385" role="group" aria-label="Card front">
    <defs>
      <clipPath id="front-shape"><rect width="630" height="385" rx="26"/></clipPath>
    </defs>
    <g clip-path="url(#front-shape)">
      <rect class="card-base" width="630" height="385" fill="var(--ink)"/>
      <polygon class="stripe-orange" points="0,82 630,40 630,42 0,89" fill="var(--orange)"/>
      <polygon class="stripe-red" points="0,89 630,42 630,45 0,108" fill="var(--red)"/>
      <polygon class="panel" points="0,108 630,45 630,251 0,297" fill="var(--paper)"/>
      <polygon class="stripe-navy" points="0,297 630,251 630,270 0,306" fill="var(--navy)"/>
      <polygon class="stripe-cyan" points="0,306 630,270 630,276 0,306" fill="var(--cyan)"/>
    </g>
    <g transform="rotate(-4 60 130)">
      <text class="tagline" x="58" y="131" font-size="16" textLength="276" lengthAdjust="spacingAndGlyphs">PRESCRIPTION AT A DISCOUNT</text>
      <text class="brand-name" x="58" y="262" font-size="118" textLength="500" lengthAdjust="spacingAndGlyphs">MedaSave</text>
    </g>
    <text class="notice" x="312" y="333" font-size="12" text-anchor="middle" letter-spacing="0.3">CHECK CURRENT PRICING ON OUR WEBSITE</text>
    <text class="web-address" x="315" y="358" font-size="21" text-anchor="middle">MedaSave.com</text>
  </svg>

  <svg class="card card--back" viewBox="0 0 630 385" role="group" aria-label="Card back">
    <defs>
      <clipPath id="back-shape"><rect width="630" height="385" rx="26"/></clipPath>
    </defs>
    <g clip-path="url(#back-shape)">
      <rect class="card-base" width="630" height="385" fill="var(--ink)"/>
      <polygon class="stripe-orange" points="0,83 274,67 274,69 0,90" fill="var(--orange)"/>
      <polygon class="stripe-red" points="0,90 274,69 296,70 296,76 0,100" fill="var(--red)"/>
      <polygon class="panel" points="0,100 296,76 296,277 0,297" fill="var(--paper)"/>
      <polygon class="stripe-navy" points="0,297 296,277 296,287 0,305" fill="var(--navy)"/>
      <polygon class="stripe-cyan" points="0,305 296,287 296,292 0,306" fill="var(--cyan)"/>

      <g class="features">
        <path d="M252,0 H630 V25 H260 a8,8 0 0 1 -8,-8 Z" fill="var(--violet)"/>
        <path d="M265,25 H630 V50 H273 a8,8 0 0 1 -8,-8 Z" fill="var(--navy)"/>
        <path d="M273,50 H630 V73 H281 a8,8 0 0 1 -8,-8 Z" fill="var(--violet)"/>
        <path d="M281,73 H630 V98 H289 a8,8 0 0 1 -8,-8 Z" fill="var(--navy)"/>
        <polygon points="273,7 284,13 273,19" fill="var(--white)"/>
        <polygon points="285,31 296,37 285,43" fill="var(--white)"/>
        <polygon points="298,55 309,61 298,67" fill="var(--white)"/>
        <polygon points="303,79 314,85 303,91" fill="var(--white)"/>
        <text class="feature" x="297" y="19">SAVE UP TO 99%</text>
        <text class="feature" x="309" y="43">100% HIPAA COMPLIANT</text>
        <text class="feature" x="322" y="67">LOWER PRICE GUARANTEE</text>
        <text class="feature" x="327" y="91">COVERS 90 DAYS SUPPLY &amp; PET MEDS</text>
      </g>
    </g>

    <g transform="rotate(-4 25 165)">
      <text class="tagline" x="25" y="165" font-size="9" textLength="152" lengthAdjust="spacingAndGlyphs">PRESCRIPTION AT A DISCOUNT</text>
      <text class="brand-name" x="25" y="236" font-size="64" textLength="244" lengthAdjust="spacingAndGlyphs">MedaSave</text>
    </g>

    <g class="processing">
      <rect class="processing-panel" x="316" y="122" width="298" height="148" rx="8" fill="var(--info-panel)"/>
      <text class="proc-label" x="334" y="154">BIN</text>
      <text class="proc-label" x="455" y="154">:</text>
      <text class="proc-value" x="478" y="154">014720</text>
      <text class="proc-label" x="334" y="180">PCN</text>
      <text class="proc-label" x="455" y="180">:</text>
      <text class="proc-value" x="478" y="180">MDSV2</text>
      <text class="proc-label" x="334" y="206">GRP</text>
      <text class="proc-label" x="455" y="206">:</text>
      <text class="proc-value" x="478" y="206">MEDASAVE</text>
      <text class="proc-label" x="334" y="232">ID</text>
      <text class="proc-label" x="455" y="232">:</text>
      <text class="proc-value" x="478" y="232">MS0000</text>
      <text class="proc-label" x="334" y="258">CONDOR</text>
      <text class="proc-label" x="455" y="258">:</text>
      <text class="proc-value" x="478" y="258">41290</text>
    </g>

    <text class="pharmacy-title" x="330" y="334" text-anchor="middle">ATTENTION PHARMACY</text>
    <text class="pharmacy-note" x="77" y="350">If you are unable to process prescription through our program please call <tspan class="strong">(800) - 555 - 0142</tspan></text>
    <text class="pharmacy-note" x="77" y="365">Administrated by Halden Health - This is <tspan class="strong">NOT INSURANCE</tspan></text>
  </svg>

  <p class="side-label side-label--front">FRONT</p>
  <p class="side-label side-label--back">BEHIND</p>

</main>
</body>
</html>
```